We need an attractive business card design that is modern and inviting. We like the blue and yellow (or gold) colors that are displayed with the logo. The business should communicate trust, experience, and integrity.

Target Market(s)

Residential and Commercial

Industry/Entity Type

Business

Contact Information for Business Card

Recessed Lighting
LED Retro Fit
Sign Repair
Alarms and Cameras
Mobile Home Services
24hr service calls

Font styles to use
Serif
Sans Serif

Colors
3176b5
0455a3
fece3e
fbee3e

Requirements
Must have
• Brannick Electric
• Owner: Marcus Brannick
• Licensed and Insured
• TECL #58731
Nice to have
• Exquisite Detail!!
• Over 20 years of experience
Should not have
• Nothing boring or traditional!!!

```html
<!DOCTYPE html>
<html lang="en">
<head>
<meta charset="utf-8">
<title>Brannick Electric – Business Card</title>
<link href="https://fonts.googleapis.com/css2?family=Source+Sans+3:wght@400;600;700&display=swap" rel="stylesheet">
<style>
  :root {
    --stage: #000000;
    --blue-top: #1c5cb0;
    --blue-bottom: #0b316a;
    --ring-blue: #1f72e6;
    --charcoal: #333333;
    --yellow: #f4e628;
    --white: #ffffff;
    --text-light: #f2f2f2;
  }
  * { margin: 0; padding: 0; box-sizing: border-box; }
  html, body {
    width: 1200px; height: 900px; overflow: hidden;
    background: var(--stage);
    font-family: "Source Sans 3", "Myriad Pro", Arial, sans-serif;
  }
  .stage { position: relative; width: 1200px; height: 900px; }

  .card { position: absolute; top: 200px; width: 310px; height: 502px; overflow: hidden; }

  /* Front: contact side */
  .card-front {
    left: 265px;
    background: linear-gradient(180deg, var(--blue-top) 0%, #1650a0 45%, var(--blue-bottom) 100%);
    border-radius: 70px 0 70px 0;
  }
  .front-ring { position: absolute; left: 0; top: 0; }
  .owner-name {
    position: absolute; left: 23px; top: 199px;
    color: var(--yellow); font-size: 22px; font-weight: 600; letter-spacing: 0.2px;
  }
  .owner-title {
    position: absolute; left: 23px; top: 227px;
    color: var(--white); font-size: 16px; font-weight: 700;
  }
  .credentials {
    position: absolute; left: 23px; top: 276px;
    color: var(--text-light); font-size: 14px; line-height: 18px;
  }
  .contact-list { position: absolute; left: 23px; top: 336px; list-style: none; }
  .contact-list li {
    display: flex; align-items: center; gap: 6px;
    color: var(--white); font-size: 14px; line-height: 20px;
  }
  .contact-list svg { flex: none; }
  .experience {
    position: absolute; left: 23px; top: 401px;
    color: var(--white); font-size: 14px; font-weight: 700; letter-spacing: 0.2px;
  }

  /* Back: services side */
  .card-back {
    left: 641px;
    background: var(--charcoal);
    border-radius: 0 70px 0 70px;
  }
  .brand-mark {
    position: absolute; left: 121px; top: 82px;
    width: 68px; height: 68px; border-radius: 50%;
    border: 3px solid var(--yellow);
  }
  .brand-name {
    position: absolute; left: 0; right: 0; top: 146px;
    text-align: center; color: var(--yellow);
    font-size: 29px; font-weight: 700; letter-spacing: 0.5px;
  }
  .service-list {
    position: absolute; left: 22px; top: 232px; list-style: none;
    color: var(--text-light); font-size: 18px; line-height: 26.5px;
  }
</style>
</head>
<body>
<main class="stage">

  <section class="card card-front" aria-label="Business card front">
    <svg class="front-ring" width="310" height="260" viewBox="0 0 310 260" aria-hidden="true">
      <circle cx="140" cy="95" r="118" fill="none" stroke="var(--ring-blue)" stroke-width="22" opacity="0.55"/>
    </svg>
    <h1 class="owner-name">MARCUS BRANNICK</h1>
    <p class="owner-title">OWNER</p>
    <p class="credentials">Licensed &amp; Insured<br>TECL #58731</p>
    <ul class="contact-list">
      <li>
        <svg width="9" height="12" viewBox="0 0 9 12" aria-hidden="true"><rect x="1" y="0.5" width="7" height="11" rx="1.5" fill="none" stroke="var(--yellow)" stroke-width="1.4"/><rect x="3.5" y="9" width="2" height="1" fill="var(--yellow)"/></svg>
        13572468
      </li>
      <li>
        <svg width="10" height="8" viewBox="0 0 10 8" aria-hidden="true"><rect x="0" y="0" width="10" height="8" rx="1" fill="var(--yellow)"/><path d="M0.5 0.8 L5 4.5 L9.5 0.8" fill="none" stroke="var(--blue-bottom)" stroke-width="1"/></svg>
        info@brannickelectric.com
      </li>
    </ul>
    <p class="experience">OVER 20 YEARS OF EXPERIENCE.</p>
  </section>

  <section class="card card-back" aria-label="Business card back">
    <div class="brand-mark" aria-hidden="true"></div>
    <h2 class="brand-name">BRANNICK ELECTRIC</h2>
    <ul class="service-list">
      <li>Residential and Commercial</li>
      <li>Recessed Lighting</li>
      <li>LED Retro Fit</li>
      <li>Sign Repair</li>
      <li>Alarms and Cameras</li>
      <li>Mobile Home Services</li>
      <li>24hr service calls</li>
    </ul>
  </section>

</main>
</body>
</html>
```